Velvet Parlour Site Make Over

I would like to get a site makeover for www.velvetparlour.example. The two main pages are the products pages eg: http://www.velvetparlour.example.au/products/marovine.html

and the home page. Please focus more on the products page as it is 10x more important than the home page.

The width of the pages should be 990px.
Updates

Target Market(s)

WOmen aged 18-35

Industry/Entity Type

Club

Requirements
Must have
• must be "pretty"

```html
<!DOCTYPE html>
<html lang="en">
<head>
<meta charset="utf-8">
<title>The Velvet Parlour – Skin Care</title>
<link rel="stylesheet" href="https://fonts.googleapis.com/css2?family=Merriweather:wght@300;400;700&display=swap">
<style>
:root{
  --bar:#222222;
  --pink:#d6168c;
  --ink:#111111;
  --white:#ffffff;
  --backdrop-a:#e4e0e6;
  --backdrop-b:#d3cdd6;
}
*{margin:0;padding:0;box-sizing:border-box}
html,body{width:1200px;height:962px;overflow:hidden}
body{position:relative;font-family:"Merriweather",Georgia,serif;color:var(--ink);background:var(--backdrop-a)}
.backdrop{position:absolute;left:0;top:64px;width:1200px;height:827px;background:linear-gradient(135deg,var(--backdrop-a),var(--backdrop-b) 50%,var(--backdrop-a))}
.topbar{position:absolute;left:0;top:0;width:1200px;height:64px;background:var(--bar)}
.topbar a{position:absolute;top:36px;color:var(--white);font-size:15px;text-decoration:none;line-height:1}
.topbar a.current{font-weight:700}
.logo{position:absolute;left:69px;top:102px;width:312px;height:53px;border-top:1.5px solid var(--pink);border-bottom:1.5px solid var(--pink);color:var(--pink);font-size:34px;font-weight:300;line-height:51px;white-space:nowrap;letter-spacing:1px}
.tagline{position:absolute;left:69px;top:160px;width:312px;text-align:center;color:var(--pink);font-size:12px;white-space:nowrap}
.search{position:absolute;left:846px;top:80px;width:242px;height:27px;background:var(--white);color:#888;font-size:15px;line-height:27px;padding-left:6px}
.search-go{position:absolute;left:1097px;top:80px;width:28px;height:27px;background:var(--white)}
.account-links a{position:absolute;top:113px;color:var(--pink);font-size:13px;text-decoration:none}
.panel{position:absolute;left:69px;top:202px;width:1056px;height:689px;background:var(--white)}
.menu a{position:absolute;left:112px;color:var(--pink);font-size:25px;font-weight:300;text-decoration:none;line-height:1}
.menu a.current{font-weight:700}
.menu i{position:absolute;left:114px;width:166px;height:1.5px;background:var(--pink)}
.product{position:absolute;width:180px}
.product .shot{position:absolute;left:10px;width:130px;height:135px;border-radius:8px}
.shot.gold{background:linear-gradient(180deg,#efe9d2,#d8c98a)}
.shot.tan{background:linear-gradient(180deg,#c4a985,#a88a66 70%,#efefef)}
.shot.white{background:linear-gradient(180deg,#f4f4f4,#dcdcdc)}
.shot.grey{background:linear-gradient(180deg,#dde3e6,#aab3b8)}
.product .brand{position:absolute;left:0;font-size:15px;font-weight:700;line-height:1}
.product .name{position:absolute;left:0;font-size:12.5px;line-height:15px;white-space:nowrap}
.product .price{position:absolute;left:0;font-size:14.5px;line-height:1}
.footer{position:absolute;left:0;top:891px;width:1200px;height:71px;background:var(--bar)}
.footer a{position:absolute;top:26px;color:var(--white);font-size:15px;text-decoration:none}
</style>
</head>
<body>
<div class="backdrop" role="img" aria-label="Soft lilac damask wallpaper pattern"></div>

<nav class="topbar">
  <a class="current" style="left:68px">Home</a>
  <a style="left:151px">Shop Online</a>
  <a style="left:279px">Shipping</a>
  <a style="left:385px">About Us</a>
  <a style="left:491px">Contact Us</a>
  <a style="left:821px">My Account</a>
  <a style="left:946px">My Wishlist</a>
  <a style="left:1068px">My Cart</a>
</nav>

<div class="logo">The Velvet Parlour</div>
<div class="tagline">Where Every Beauty Lover Belongs</div>

<div class="search">Search...</div>
<svg class="search-go" viewBox="0 0 28 27"><path d="M6 6 L23 13.5 L6 21 L9 13.5 Z" fill="var(--pink)"/></svg>
<div class="account-links">
  <a style="left:853px">REGISTER</a>
  <a style="left:947px">LOGIN</a>
</div>

<main class="panel"></main>

<nav class="menu">
  <a style="top:278px">HAIR CARE</a><i style="top:327px"></i>
  <a class="current" style="top:348px">SKIN CARE</a><i style="top:396px"></i>
  <a style="top:422px">FRAGRANCES</a><i style="top:469px"></i>
  <a style="top:495px">MAKE UP</a><i style="top:542px"></i>
  <a style="top:567px">BLOG</a><i style="top:616px"></i>
  <a style="top:643px">FORUM</a><i style="top:687px"></i>
</nav>

<section class="products">
  <div class="product" style="left:347px;top:0">
    <div class="shot gold" style="top:293px" role="img" aria-label="Vitamin C serum bottle with box"></div>
    <span class="brand" style="top:444px">Lunessa</span>
    <span class="name" style="top:459px">Cellara C 12<br>Topical Vitamin C</span>
    <span class="price" style="top:488px">$79.05</span>
  </div>
  <div class="product" style="left:538px;top:0">
    <div class="shot tan" style="top:293px" role="img" aria-label="Tinted sunscreen tube, light"></div>
    <span class="brand" style="top:444px">Lunessa</span>
    <span class="name" style="top:459px">Cellara TintGuard<br>SPF30 Light</span>
    <span class="price" style="top:488px">$32.71</span>
  </div>
  <div class="product" style="left:730px;top:0">
    <div class="shot tan" style="top:293px" role="img" aria-label="Tinted sunscreen tube, dark"></div>
    <span class="brand" style="top:444px">Lunessa</span>
    <span class="name" style="top:459px">TintGuard SPF30 Dark</span>
    <span class="price" style="top:473px">$32.71</span>
  </div>
  <div class="product" style="left:918px;top:0">
    <div class="shot tan" style="top:293px" role="img" aria-label="Tinted sunscreen tube, medium"></div>
    <span class="brand" style="top:444px">Lunessa</span>
    <span class="name" style="top:459px">TintGuard SPF30<br>&nbsp;Medium</span>
    <span class="price" style="top:488px">$32.71</span>
  </div>

  <div class="product" style="left:347px;top:0">
    <div class="shot white" style="top:530px" role="img" aria-label="White cleanser bottle"></div>
    <span class="brand" style="top:677px">Lunessa</span>
    <span class="name" style="top:692px">Dual Cleanser</span>
    <span class="price" style="top:706px">$27.26</span>
  </div>
  <div class="product" style="left:540px;top:0">
    <div class="shot gold" style="top:530px" role="img" aria-label="Brightening cream bottle with box"></div>
    <span class="brand" style="top:677px">Lunessa</span>
    <span class="name" style="top:692px">Lumira Skin Bleaching<br>Cream</span>
    <span class="price" style="top:721px">$79.05</span>
  </div>
  <div class="product" style="left:728px;top:0">
    <div class="shot grey" style="top:530px" role="img" aria-label="Exfoliating cleanser bottle"></div>
    <span class="brand" style="top:677px">Lunessa</span>
    <span class="name" style="top:692px">Exfoliating Cleanser</span>
    <span class="price" style="top:706px">$27.26</span>
  </div>
  <div class="product" style="left:916px;top:0">
    <div class="shot grey" style="top:530px" role="img" aria-label="Exfoliating cleanser bottle"></div>
    <span class="brand" style="top:677px">Lunessa</span>
    <span class="name" style="top:692px">Exfoliating Cleanser</span>
    <span class="price" style="top:706px">$27.26</span>
  </div>
</section>

<footer class="footer">
  <a style="left:345px">Terms and Conditions</a>
  <a style="left:544px">Sitemap</a>
  <a style="left:640px">Privacy Policy</a>
  <a style="left:779px">Contact Us</a>
</footer>
</body>
</html>
```